Dating Coach needs a Book Cover Design

My new book called "When to Turn the Tide: Meeting Romance Among the Endless Crowd of Digital Courtship" needs a cover! I tried to make one on my own, but it's just not my skill set :) Please see attached for my best attempt. I'd like to see the title smaller and the tagline bigger - so that the tagline is easier to read. But I'm not sure how to do this and still have the Title look great. I'm also considering if the "TURN THE TIDE" part should not be in all caps. Looking forward to your ideas! I'm also afraid that the drawing is a bit too cartoonish and doesn't match my brand. I'm looking for something elegant and also very approachable and down to earth. My website is www.petrawendtcoaching.example so you can use as reference! Please see my attached brand style guide for colors. This will be an e-book that I give away for free to anyone who signs up for my newsletter. Some mock-ups would also be great to use in advertising.

```html
<!DOCTYPE html>
<html lang="en">
<head>
<meta charset="utf-8">
<title>When to Turn the Tide – Book Cover Wrap</title>
<link href="https://fonts.googleapis.com/css2?family=Allura&family=Cormorant+Garamond:wght@500;600&family=Montserrat:wght@400;500;600&display=swap" rel="stylesheet">
<style>
  :root{
    --backdrop:#ece6df;
    --paper:#f6f2ec;
    --plum:#6f4a7e;
    --plum-deep:#5e3f6b;
    --ink:#3f3640;
    --rule:#cbbfc9;
    --cream-text:#f4eef5;
    --photo-light:#f1ebe4;
    --photo-mid:#e6dbd0;
    --photo-blush:#f2c9c2;
  }
  *{box-sizing:border-box;margin:0;padding:0}
  html,body{width:1200px;height:800px;overflow:hidden}
  body{background:var(--backdrop);font-family:"Montserrat",sans-serif;color:var(--ink);position:relative}

  .wrap{position:absolute;top:70px;left:112px;display:flex;gap:32px;height:660px}

  /* Back cover */
  .back-cover{width:420px;height:660px;background:var(--paper);position:relative;display:flex;flex-direction:column;box-shadow:0 2px 10px rgba(80,60,70,.12)}
  .back-body{flex:1;padding:36px 40px 0;text-align:center}
  .heart-mark{width:30px;height:30px;stroke:var(--plum);fill:none;stroke-width:1.6}
  .back-headline{font-family:"Cormorant Garamond",serif;font-weight:600;font-size:20px;line-height:1.3;color:var(--ink);margin-top:14px}
  .back-intro{font-size:11px;line-height:1.6;text-align:left;margin-top:18px;color:var(--ink)}
  .benefits{list-style:none;margin:14px 36px 0 24px;text-align:left}
  .benefit{display:flex;gap:26px;padding:11px 0 9px;border-bottom:1px solid var(--rule)}
  .benefit:last-child{border-bottom:none}
  .benefit-icon{width:36px;height:34px;flex:none;stroke:var(--plum);fill:none;stroke-width:1.6;stroke-linecap:round;stroke-linejoin:round}
  .benefit-title{font-size:11.5px;font-weight:500;letter-spacing:.16em;color:var(--plum)}
  .benefit-text{font-size:10.5px;line-height:1.5;margin-top:3px;color:var(--ink)}
  .back-quote{font-family:"Allura",cursive;font-size:23px;line-height:1.2;color:var(--plum);margin-top:10px}
  .back-quote .heart-mark{width:18px;height:18px;margin-top:2px}
  .back-band{height:128px;background:var(--plum);color:var(--cream-text);text-align:center;padding-top:24px}
  .band-name{font-size:13px;letter-spacing:.16em;font-weight:500}
  .band-line{font-size:11.5px;line-height:1.6;margin-top:8px;opacity:.92}
  .band-site{font-size:11.5px;letter-spacing:.04em;margin-top:8px}

  /* Spine */
  .spine{width:58px;height:660px;background:var(--plum);color:var(--cream-text);display:flex;flex-direction:column;align-items:center;padding-top:44px}
  .spine .heart-solid{width:26px;height:24px;fill:var(--cream-text)}
  .spine-text{writing-mode:vertical-rl;display:flex;align-items:center;gap:16px;margin-top:10px}
  .spine-title{font-family:"Cormorant Garamond",serif;font-weight:600;font-size:27px}
  .spine-author{font-family:"Cormorant Garamond",serif;font-weight:500;font-size:19px}
  .spine-dash{width:1px;height:18px;background:var(--cream-text)}

  /* Front cover */
  .front-cover{width:430px;height:660px;background:var(--paper);position:relative;overflow:hidden;text-align:center;box-shadow:0 2px 10px rgba(80,60,70,.12)}
  .front-photo{position:absolute;left:0;right:0;top:300px;height:290px;background:
      radial-gradient(ellipse 80px 60px at 70px 170px,var(--photo-blush),transparent 75%),
      radial-gradient(ellipse 120px 110px at 330px 175px,#e9e0d6,transparent 80%),
      linear-gradient(180deg,var(--paper) 0%,var(--photo-light) 30%,var(--photo-mid) 70%,var(--paper) 100%)}
  .front-type{position:relative;padding-top:42px}
  .title-lead{font-family:"Allura",cursive;font-size:76px;line-height:.9;color:var(--plum);margin-left:60px}
  .title-main{font-family:"Cormorant Garamond",serif;font-weight:600;font-size:56px;line-height:1;color:var(--plum-deep);margin-top:2px}
  .divider{display:flex;align-items:center;justify-content:center;gap:10px;margin-top:14px}
  .divider-rule{width:62px;height:1px;background:var(--plum)}
  .divider .heart-mark{width:28px;height:28px}
  .subtitle{font-size:16px;font-weight:600;letter-spacing:.12em;line-height:1.6;color:var(--plum);margin-top:12px}
  .subtitle-script{font-family:"Allura",cursive;font-size:66px;line-height:1;color:var(--plum-deep);margin-top:-2px}
  .swash{display:block;margin:0 auto;width:170px;height:12px}
  .author{position:absolute;left:0;right:0;bottom:24px}
  .author-name{font-family:"Cormorant Garamond",serif;font-weight:600;font-size:36px;color:var(--plum-deep);line-height:1}
  .author-tag{display:flex;align-items:center;justify-content:center;gap:12px;font-size:12.5px;letter-spacing:.3em;color:var(--plum);margin-top:6px}
  .author-tag .divider-rule{width:54px}
</style>
</head>
<body>
<svg width="0" height="0" style="position:absolute">
  <defs>
    <path id="heart" d="M12 21s-7.5-4.8-9.3-9.6C1.4 7.8 4 4.5 7.3 4.5c2 0 3.6 1.2 4.7 2.9 1.1-1.7 2.7-2.9 4.7-2.9 3.3 0 5.9 3.3 4.6 6.9C19.5 16.2 12 21 12 21z"/>
  </defs>
</svg>

<main class="wrap">
  <!-- Back cover -->
  <section class="back-cover">
    <div class="back-body">
      <svg class="heart-mark" viewBox="0 0 24 24"><use href="#heart"/></svg>
      <h2 class="back-headline">Online dating can feel<br>like looking for a needle in a haystack.</h2>
      <p class="back-intro">This guide will help you cut through the noise, avoid the overwhelm, and focus on what really matters—so you can find genuine connection and lasting love.</p>
      <ul class="benefits">
        <li class="benefit">
          <svg class="benefit-icon" viewBox="0 0 36 34"><circle cx="15" cy="14" r="10"/><path d="M22 21l9 9M9 13a6 6 0 0 1 5-5"/></svg>
          <div><div class="benefit-title">CLARITY</div><div class="benefit-text">Discover what you truly want<br>and deserve.</div></div>
        </li>
        <li class="benefit">
          <svg class="benefit-icon" viewBox="0 0 24 24"><use href="#heart"/></svg>
          <div><div class="benefit-title">CONFIDENCE</div><div class="benefit-text">Show up authentically and attract<br>the right matches.</div></div>
        </li>
        <li class="benefit">
          <svg class="benefit-icon" viewBox="0 0 36 34"><path d="M4 5h28L21 18v12l-6-3v-9z"/></svg>
          <div><div class="benefit-title">DISCERNMENT</div><div class="benefit-text">Learn how to spot potential and<br>avoid wasting time.</div></div>
        </li>
        <li class="benefit">
          <svg class="benefit-icon" viewBox="0 0 36 34"><circle cx="11" cy="9" r="4"/><circle cx="25" cy="9" r="4"/><circle cx="18" cy="18" r="4"/><path d="M3 26c0-5 3-8 8-8M33 26c0-5-3-8-8-8M9 31c0-5 4-8 9-8s9 3 9 8z"/></svg>
          <div><div class="benefit-title">CONNECTION</div><div class="benefit-text">Build meaningful relationships<br>that last.</div></div>
        </li>
      </ul>
      <p class="back-quote">You're not looking for more dates.<br>You're looking for the one.<br><svg class="heart-mark" viewBox="0 0 24 24"><use href="#heart"/></svg></p>
    </div>
    <footer class="back-band">
      <div class="band-name">PETRA WENDT COACHING</div>
      <div class="band-line">Helping women find clarity, confidence<br>and real love—online and in life.</div>
      <div class="band-site">www.petrawendtcoaching.example</div>
    </footer>
  </section>

  <!-- Spine -->
  <section class="spine">
    <svg class="heart-solid" viewBox="0 0 24 24"><use href="#heart"/></svg>
    <div class="spine-text">
      <span class="spine-dash"></span>
      <span class="spine-title">When to Turn the Tide</span>
      <span class="spine-dash"></span>
      <span class="spine-author">Petra Wendt Coaching</span>
    </div>
  </section>

  <!-- Front cover -->
  <section class="front-cover">
    <div class="front-photo" role="img" aria-label="Soft-focus still life of a pale pink peony, a smartphone and a speckled mug with a heart on a cream table"></div>
    <div class="front-type">
      <h1>
        <span class="title-lead">When to</span>
        <span class="title-main" style="display:block">Turn the Tide</span>
      </h1>
      <div class="divider">
        <span class="divider-rule"></span>
        <svg class="heart-mark" viewBox="0 0 24 24"><use href="#heart"/></svg>
        <span class="divider-rule"></span>
      </div>
      <p class="subtitle">MEETING ROMANCE AMONG THE<br>ENDLESS CROWD OF</p>
      <p class="subtitle-script">Digital Courtship</p>
      <svg class="swash" viewBox="0 0 170 12"><path d="M2 10C50 4 110 3 168 5" stroke="var(--plum-deep)" stroke-width="2.4" fill="none" stroke-linecap="round"/></svg>
    </div>
    <div class="author">
      <div class="author-name">Petra Wendt</div>
      <div class="author-tag"><span class="divider-rule"></span>COACHING<span class="divider-rule"></span></div>
    </div>
  </section>
</main>
</body>
</html>
```